Stage Design Company Business Card

We are looking to step up up our business card design for our team.

We are a Full service Design and Consultation company for Stage and TV with an emphasis in Theatrical Lighting.

We like our materials to be clean and modern with solid colors free of patterns and gradients. Our brand consists of 4 primary colors Purple, Black, Grey, and White. Provided is our Word Mark as well as our Symbol Logo.

We would like our cards to leave an impression beyond the information, show our attention to design and detail, and make our marks an easily recognized feature (together or apart) for our clients.

We need a warm approachable comfortable feel for some clients, and a professional flair for the board member type clients.

Attached are our brand elements, and our existing cards to give a sense of our style and a glipse at the information we provide on our cards.

Target Market(s)

broad client base from church leaders to high school teachers and architects.

Industry/Entity Type

Business

Contact Information for Business Card

We format our phone number with periods not parenthesis or dashes. Information will be edited for each of our team members, and team member specific cards are not part of this scope, but rather a template so to speak.

Font styles to use
Sans Serif

Colors
6b449b
ffffff
000000
333333
aaaaaa

Requirements
Must have
• Wordmark and logo mark present (does not need to exist on the same side of card)
• Brand Colors,
• Name, Phone, Email, Address.
• Unique choices that make someone stop and take a second look
Nice to have
• It would be nice to somehow convey what we DO, as our brand name does not lend itself to this, outside of an obvious tagline though.....
• social media if not crowded. all of our handles match (instagram, twitter, facebook)
Should not have
• "clipart"

```html
<!DOCTYPE html>
<html lang="en">
<head>
<meta charset="utf-8">
<title>Business Card – Front</title>
<link rel="stylesheet" href="https://fonts.googleapis.com/css2?family=Open+Sans:wght@400;600;700&display=swap">
<style>
  :root {
    --page-bg: #e8e6ec;
    --card-purple: #37226b;
    --text-light: #f1eff6;
    --text-name: #d9d5e4;
    --disc-silver: #ecebee;
    --disc-edge: #d6d4db;
    --brand-purple: #3a2372;
  }
  * { margin: 0; padding: 0; box-sizing: border-box; }
  html, body {
    width: 1200px;
    height: 900px;
    overflow: hidden;
    background: var(--page-bg);
    font-family: "Open Sans", Arial, sans-serif;
  }
  .business-card {
    position: absolute;
    left: 120px;
    top: 153px;
    width: 960px;
    height: 594px;
    background: var(--card-purple);
    color: var(--text-light);
  }
  .person {
    position: absolute;
    left: 50px;
    top: 62px;
  }
  .person-name {
    font-weight: 700;
    font-size: 30px;
    line-height: 1.1;
    letter-spacing: 0.2px;
    color: var(--text-name);
  }
  .person-role {
    font-weight: 400;
    font-size: 23px;
    line-height: 1.4;
  }
  .contact-list {
    position: absolute;
    left: 50px;
    top: 324px;
    list-style: none;
  }
  .contact-item {
    display: flex;
    align-items: center;
    height: 35.5px;
    font-size: 24px;
  }
  .contact-icon {
    width: 20px;
    height: 20px;
    margin-right: 12px;
    fill: var(--text-light);
    flex: none;
  }
  .address {
    position: absolute;
    left: 50px;
    top: 452px;
    font-size: 24px;
    line-height: 35px;
    font-style: normal;
  }
  .brand-disc {
    position: absolute;
    left: 454px;
    top: 65px;
    width: 464px;
    height: 464px;
    border-radius: 50%;
    background: var(--disc-silver);
    box-shadow: inset 0 0 0 2px var(--disc-edge);
    display: flex;
    align-items: center;
    justify-content: center;
  }
  .brand-name {
    font-weight: 600;
    font-size: 46px;
    letter-spacing: 14px;
    margin-right: -14px;
    color: var(--brand-purple);
  }
</style>
</head>
<body>
  <section class="business-card">
    <div class="person">
      <p class="person-name">DANIEL WHITMORE</p>
      <p class="person-role">Managing Director</p>
    </div>

    <ul class="contact-list">
      <li class="contact-item">
        <svg class="contact-icon" viewBox="0 0 20 20" aria-hidden="true"><path d="M4.2 2.5l3 .2 1.3 3.6-1.9 1.4a10 10 0 0 0 5.7 5.7l1.4-1.9 3.6 1.3.2 3c-.2.9-1 1.4-2 1.4C8.5 17.2 2.8 11.5 2.8 4.5c0-1 .5-1.8 1.4-2z"/></svg>
        (055)987654321
      </li>
      <li class="contact-item">
        <svg class="contact-icon" viewBox="0 0 20 20" aria-hidden="true"><path d="M2 4.5h16v11H2z M3.5 6l6.5 5 6.5-5" stroke="var(--card-purple)" stroke-width="1.3"/></svg>
        contact@lumora.com
      </li>
      <li class="contact-item">
        <svg class="contact-icon" viewBox="0 0 20 20" aria-hidden="true"><circle cx="10" cy="10" r="8"/><path d="M6 6.5l3 1-1 3 2 2-1 3M12.5 4.5l1 2.5 2.5.5" stroke="var(--card-purple)" stroke-width="1.3" fill="none"/></svg>
        www.lumorastage.com
      </li>
    </ul>

    <address class="address">4821, Harbor Lane West,<br>Northvale, 60418</address>

    <div class="brand-disc">
      <span class="brand-name">LUMORA</span>
    </div>
  </section>
</body>
</html>
```